依頼詳細
作りたいチラシのイメージは、「参考画像.jpg」の通りです。

裏面のデザイン(価格表)は完成しておりますので、デザインの雰囲気をなるべく合わせていただけると幸いです。(「裏面画像.jpg」)
また、以前に表面のデザインも作成しておりますので、こちらも参考にしてください。(「表面画像.jpg」)

特に、
・往診料無料
・ワクチン料金
・フィラリア症予防薬料金
・自宅で手軽に予防ができる
上記の内容をより訴求できるデザインにしたいと思っております。

動物病院ですので、優しく、特に女性受けが良さそうなイメージで作成をお願いいたします。

使用する色は、主に「緑、オレンジ」をメインに考えておりますが、色の具合は自由に調節いただいて結構です。
作りたいチラシのイメージは、「参考画像.jpg」の通りですが、デザインは自由に調節していただいて結構です。
また、こちらで用意させていただく素材以外で、デザインに沿った文言・イラスト・アイコン・写真などがありましたら、自由に取り入れていただければと思います。
記載項目
・チラシに使用する文章はこちらで用意いたします。

「参考画像.jpg」の①~⑩にはPDFファイル(チラシ記載内容.pdf)に記載されている文章を使用してください。

・院長の画像については、画像1、画像2のいずれかをお使いください。
※psd形式以外のデータをご希望の際はお申し付けください。

・ロゴについては画像3をお使いください。
サイズ
A4
ページ数
片面
希望イメージ
• +5 0 +5
• シンプル
複雑
• 単色
カラフル
• 暗い
明るい
• 日常
高級
• 遊び心
厳粛
• 未来的
伝統的
• 女性的
男性的
希望する色
納品ファイル
• 高解像度JPG (.jpg)
• イラストレーター形式 (.ai)
補足説明
依頼公開後の追記内容
■ 選んだ理由

全体的なイメージと、特に家のデザインが気に入りました。

■ 提案者全員のお礼・コメント

この度はご提案くださり誠にありがとうございました。
どれも良いものばかりで、選択に非常に迷いました。

また機会がございましたら、その時はどうぞよろしくお願いいたします。

```html
<!DOCTYPE html>
<html lang="ja">
<head>
<meta charset="utf-8">
<title>ひだまり動物病院 往診チラシ</title>
<link href="https://fonts.googleapis.com/css2?family=M+PLUS+Rounded+1c:wght@500;700;800&family=Noto+Sans+JP:wght@400;500;700;900&display=swap" rel="stylesheet">
<style>
:root{
  --bg:#eef6e4;
  --green:#5cb531;
  --green-dark:#2f7d1e;
  --green-light:#dcefcb;
  --orange:#f29a2e;
  --orange-light:#fde9cf;
  --red:#e5483a;
  --sky:#6fb9e0;
  --sky-light:#e3f2fa;
  --ink:#3a3a3a;
  --white:#ffffff;
}
*{box-sizing:border-box;margin:0;padding:0}
html,body{width:889px;height:1200px;overflow:hidden}
body{background:var(--bg);font-family:"Noto Sans JP",sans-serif;color:var(--ink);position:relative}

.tabs{position:absolute;top:28px;left:0;width:100%;display:flex;justify-content:center;gap:44px}
.tab{background:var(--green);color:var(--white);font-family:"M PLUS Rounded 1c",sans-serif;font-weight:800;font-size:28px;line-height:40px;padding:6px 34px;border-radius:10px}

.doctor{position:absolute;left:24px;top:100px;width:262px;height:318px;border-radius:14px;background:linear-gradient(180deg,#d9d2c4 0%,#c7bfb0 55%,#2c3c58 100%)}
.doctor-bubble{position:absolute;left:34px;top:110px;background:var(--white);color:var(--green-dark);font-size:14px;font-weight:700;padding:5px 12px;border-radius:16px;border:2px solid var(--green)}
.doctor-name{position:absolute;left:150px;top:384px;background:var(--white);font-size:13px;padding:2px 10px;border-radius:4px}

.house{position:absolute;left:300px;top:100px;width:565px;height:260px}
.headline{position:absolute;left:300px;top:150px;width:565px;text-align:center;font-family:"M PLUS Rounded 1c",sans-serif;font-weight:800;color:var(--green-dark)}
.headline .l1{font-size:56px;line-height:64px;letter-spacing:2px}
.headline .l1 em{font-style:normal;color:var(--orange)}
.headline .l2{font-size:42px;line-height:54px;padding-left:150px}
.pets{position:absolute;border-radius:50%}
.pets.dog{left:770px;top:112px;width:84px;height:72px;background:#f4c28a}
.pets.cat{left:716px;top:100px;width:56px;height:52px;background:#f2b57b}

.free{position:absolute;left:300px;top:370px;width:565px;display:flex;align-items:center;justify-content:center;gap:4px;font-family:"M PLUS Rounded 1c",sans-serif;font-weight:800;font-size:32px;color:var(--green-dark)}
.free .box{background:var(--red);color:var(--white);width:44px;height:44px;display:flex;align-items:center;justify-content:center;border-radius:4px}
.free .gap{width:10px}

.price{position:absolute;top:432px;background:var(--white);border-radius:10px;overflow:hidden}
.price-head{color:var(--white);font-weight:700;font-size:18px;line-height:22px;text-align:center;padding:5px 0}
.vaccine{left:24px;width:420px}
.vaccine .price-head{background:var(--green)}
.filaria{left:456px;width:410px}
.filaria .price-head{background:var(--orange)}
.vac-group{display:flex;border-top:2px solid var(--white)}
.vac-kind{width:76px;display:flex;align-items:center;justify-content:center;font-weight:700;font-size:17px;background:var(--green-light);color:var(--green-dark)}
.vac-list{flex:1;padding:2px 14px;list-style:none}
.vac-list li{display:flex;justify-content:space-between;font-size:15px;line-height:18px;padding:4px 0;border-bottom:1px dotted #bbb}
.vac-list li:last-child{border-bottom:none}
.vac-list b{color:var(--red);font-weight:700}
.fil-table{width:100%;border-collapse:collapse;font-size:15px}
.fil-table th{background:var(--orange-light);font-weight:500;font-size:13px;line-height:18px;padding:3px 4px}
.fil-table td{padding:3px 10px;line-height:19px;border-bottom:1px dotted #bbb;text-align:right}
.fil-table tr:last-child td{border-bottom:none}
.fil-table td:first-child{text-align:left}
.fil-table .set{color:var(--red);font-weight:700}

.section-head{position:absolute;left:24px;width:842px;color:var(--white);font-weight:700;font-size:17px;line-height:24px;padding:4px 16px;border-radius:6px;background:var(--sky)}
.schedule-head{top:668px}
.area-head{top:812px;background:var(--orange)}
.grid{position:absolute;left:24px;width:842px;display:grid;grid-template-columns:repeat(5,1fr);gap:6px}
.schedule{top:704px}
.area{top:848px}
.col{background:var(--white);border-radius:6px;overflow:hidden;font-size:13px}
.col h3{font-size:14px;line-height:20px;text-align:center;padding:2px 0;background:var(--sky-light);color:#2a6f97}
.col ul{list-style:none;padding:4px 10px;line-height:20px}
.area .col{padding:8px 10px;line-height:20px;height:132px}

.footer{position:absolute;left:0;top:1004px;width:889px;height:196px;background:var(--white);border-top:6px solid var(--green)}
.footer .lead{position:absolute;left:30px;top:22px;font-size:17px;font-weight:700;color:var(--green-dark)}
.footer .tel{position:absolute;left:360px;top:14px;display:flex;align-items:center;gap:10px;font-family:"M PLUS Rounded 1c",sans-serif;font-weight:800;font-size:46px;line-height:60px;color:var(--red)}
.footer .brand{position:absolute;left:30px;top:72px;display:flex;align-items:center;gap:10px;font-family:"M PLUS Rounded 1c",sans-serif;font-weight:700;font-size:34px;line-height:44px;color:var(--green-dark)}
.brand .mark{width:32px;height:32px;border-radius:50%;background:var(--orange)}
.footer .sub{position:absolute;left:30px;top:134px;font-size:13px}
.footer .info{position:absolute;left:420px;top:90px;font-size:14px;line-height:1.7}
</style>
</head>
<body>

<div class="tabs">
  <span class="tab">自宅でワクチン</span>
  <span class="tab">自宅でフィラリア予防</span>
</div>

<div class="doctor" role="img" aria-label="紺色のスクラブを着た院長の写真"></div>
<span class="doctor-bubble">お気軽にご相談ください</span>
<span class="doctor-name">院長：森田 陽</span>

<svg class="house" viewBox="0 0 565 260" aria-hidden="true">
  <path d="M20 72 L282 8 L545 72 L545 252 L20 252 Z" fill="#ffffff" stroke="#5cb531" stroke-width="6" stroke-linejoin="round"/>
</svg>
<div class="pets dog" role="img" aria-label="犬のイラスト"></div>
<div class="pets cat" role="img" aria-label="猫のイラスト"></div>
<div class="headline">
  <div class="l1">「ワクチンは</div>
  <div class="l1"><em>おウチ</em>で」</div>
  <div class="l2">が新しい！</div>
</div>

<div class="free">
  <span class="box">往</span><span class="box">診</span><span class="box">料</span><span class="gap"></span><span class="box">無</span><span class="box">料</span>
  <span>でお伺いします！</span>
</div>

<section class="price vaccine">
  <h2 class="price-head">ワクチン料金表</h2>
  <div class="vac-group">
    <div class="vac-kind">犬用</div>
    <ul class="vac-list">
      <li>狂犬病ワクチン<b>2,500円</b></li>
      <li>9種混合ワクチン<b>5,000円</b></li>
      <li>8種混合ワクチン<b>4,800円</b></li>
      <li>6種混合ワクチン<b>4,500円</b></li>
    </ul>
  </div>
  <div class="vac-group">
    <div class="vac-kind">猫用</div>
    <ul class="vac-list">
      <li>5種混合ワクチン<b>4,000円</b></li>
      <li>3種混合ワクチン<b>3,500円</b></li>
    </ul>
  </div>
</section>

<section class="price filaria">
  <h2 class="price-head">フィラリア症予防薬料金表</h2>
  <table class="fil-table">
    <tr><th></th><th>1回分</th><th>1回分お得な6回セット</th></tr>
    <tr><td>5kgまで</td><td>600円</td><td class="set">4,200円</td></tr>
    <tr><td>5kg〜10kg</td><td>700円</td><td class="set">4,800円</td></tr>
    <tr><td>10kg〜20kg</td><td>900円</td><td class="set">6,300円</td></tr>
    <tr><td>20kg〜30kg</td><td>1,200円</td><td class="set">7,200円</td></tr>
    <tr><td>30kg〜40kg</td><td>1,500円</td><td class="set">9,100円</td></tr>
    <tr><td>40kg以上</td><td>1,700円</td><td class="set">10,500円</td></tr>
  </table>
</section>

<h2 class="section-head schedule-head">往診スケジュール</h2>
<div class="grid schedule">
  <div class="col"><h3>栃木県</h3><ul><li>4/3(月)・4/17(月)</li><li>5/1(月)・5/15(月)</li><li>5/29(月)</li></ul></div>
  <div class="col"><h3>群馬県</h3><ul><li>4/4(火)・4/18(火)</li><li>5/2(火)・5/16(火)</li><li>5/30(火)</li></ul></div>
  <div class="col"><h3>埼玉県</h3><ul><li>4/5(水)・4/19(水)</li><li>5/10(水)・5/17(水)</li><li>5/31(水)</li></ul></div>
  <div class="col"><h3>東京都</h3><ul><li>4/6(木)・4/20(木)</li><li>5/11(木)・5/18(木)</li><li>6/1(木)</li></ul></div>
  <div class="col"><h3>神奈川県</h3><ul><li>4/7(金)・4/21(金)</li><li>5/12(金)・5/19(金)</li><li>6/2(金)</li></ul></div>
</div>

<h2 class="section-head area-head">往診対応地域</h2>
<div class="grid area">
  <div class="col">足利市・佐野市・栃木市・小山市・鹿沼市・宇都宮市</div>
  <div class="col">館林市・太田市・桐生市・みどり市・伊勢崎市</div>
  <div class="col">熊谷市・行田市・加須市・羽生市・深谷市</div>
  <div class="col">全域</div>
  <div class="col">川崎市・横浜市・相模原市・大和市</div>
</div>

<footer class="footer">
  <p class="lead">往診のご予約・ご相談はこちら</p>
  <div class="tel">
    <svg width="40" height="40" viewBox="0 0 24 24" aria-hidden="true"><path fill="#e5483a" d="M6.6 10.8a15 15 0 0 0 6.6 6.6l2.2-2.2c.3-.3.7-.4 1-.2 1.1.4 2.3.6 3.6.6.6 0 1 .4 1 1V20c0 .6-.4 1-1 1C10.6 21 3 13.4 3 4c0-.6.4-1 1-1h3.5c.6 0 1 .4 1 1 0 1.3.2 2.5.6 3.6.1.3 0 .7-.2 1z"/></svg>
    <span>TEL:080-1234-5678</span>
  </div>
  <div class="brand"><span class="mark"></span>ひだまり動物病院</div>
  <p class="sub">mail：info@hidamari-vet.example</p>
  <p class="info">TEL 0284-00-1122（受付時間 9:00〜18:00）<br>〒326-0000 栃木県足利市ひだまり町1-2-3</p>
</footer>

</body>
</html>
```